Banner Ad Design Project

Design a 130x130 banner dynamic flash banner ad for China's leading business school. Banner should have 3 frames.
Frame 1 - "Expand Your Career Opportunities with the World's Largest Market of 1.3 Billion People"
(should show China here, globe, or photo of Great Wall, etc)
Frame 2 - "Do an MBA in the World's Most Dynamic Global City - Shanghai"
(have a photo here of modern Shanghai in between two doors as if someone would enter Shanghai through a doorway)
Frame 3 - "HALNU China's #1 Business School and Ranked #15 in the World by the Weekly Arbiter - Click here
(show photo of the school or school logo)

```html
<!DOCTYPE html>
<html lang="en">
<head>
<meta charset="utf-8">
<title>New Career Ahead – Banner Series</title>
<link rel="stylesheet" href="https://fonts.googleapis.com/css2?family=Open+Sans:wght@400;600;700&display=swap">
<style>
  :root {
    --sky-deep: #1c5a8f;
    --sky-mid: #5d93bf;
    --haze: #eef3f5;
    --road: #8d9296;
    --grass: #9fbf72;
    --white: #ffffff;
    --ink: #111111;
    --accent-red: #c8171e;
    --accent-blue: #1a8fe0;
    --panel-light: #eef0f6;
  }
  * { margin: 0; padding: 0; box-sizing: border-box; }
  html, body { width: 1200px; height: 369px; overflow: hidden; background: var(--white); }
  body { font-family: "Open Sans", Arial, sans-serif; }

  .board { position: relative; width: 1200px; height: 369px; overflow: hidden; }

  .board-backdrop {
    position: absolute; inset: 0;
    background:
      linear-gradient(180deg, rgba(255,255,255,0) 0%, rgba(255,255,255,0) 58%, rgba(159,191,114,0.45) 64%, rgba(141,146,150,0.85) 74%, var(--road) 100%),
      linear-gradient(90deg, var(--sky-deep) 0%, var(--sky-mid) 28%, var(--haze) 58%, var(--haze) 100%);
  }

  .headline {
    position: absolute; left: 42px; top: 268px;
    color: var(--white); font-weight: 400; font-size: 37px; letter-spacing: 0.5px;
  }

  .direction-arrow { position: absolute; left: 590px; top: 252px; }

  .frame {
    position: absolute; top: 44px; width: 164px; height: 164px; overflow: hidden;
    text-transform: uppercase;
  }
  .frame-photo { position: absolute; inset: 0; }
  .frame-copy { position: relative; text-align: left; }

  .frame--market { left: 378px; }
  .frame--market .frame-photo {
    background: linear-gradient(180deg, #9cc6ea 0%, #cfe3f2 45%, #8ba36c 78%, #5d6f45 100%);
  }
  .frame--market .frame-copy { padding: 4px 8px; }
  .frame--market .lead { color: var(--white); font-size: 18px; font-weight: 400; line-height: 20px; }
  .frame--market .body { color: var(--ink); font-size: 11.5px; font-weight: 600; line-height: 15px; }

  .frame--city { left: 638px; }
  .frame--city .frame-photo {
    background: linear-gradient(180deg, #0d3f86 0%, #3c72b9 50%, #7d8a98 78%, #1a1a1a 100%);
  }
  .frame--city .frame-copy { text-align: center; padding-top: 4px; color: var(--white); }
  .frame--city .lead { font-size: 23px; font-weight: 400; line-height: 26px; }
  .frame--city .body { font-size: 11px; font-weight: 600; line-height: 14px; }
  .frame--city .enter-arrow { position: absolute; left: 74px; bottom: 6px; }

  .frame--school { left: 902px; background: var(--panel-light); }
  .frame--school .frame-photo {
    top: auto; height: 48px;
    background: linear-gradient(180deg, #c9d6e4 0%, #b7a995 55%, #6f7d56 100%);
  }
  .frame--school .frame-copy { text-align: center; padding-top: 6px; }
  .school-name {
    display: flex; align-items: center; justify-content: center; gap: 5px;
    color: var(--accent-red); font-size: 18px; font-weight: 700; line-height: 22px;
  }
  .school-name .mark { width: 10px; height: 10px; background: var(--accent-red); }
  .frame--school .body {
    margin-top: 12px; color: var(--ink); font-size: 11px; font-weight: 600; line-height: 14px; padding: 0 6px;
  }
  .frame--school .rank { color: var(--accent-red); font-size: 15px; font-weight: 700; }
  .frame--school .cta { color: var(--accent-blue); }
</style>
</head>
<body>
<main class="board">
  <div class="board-backdrop" role="img" aria-label="Open road curving into the distance under a blue sky with green fields"></div>

  <h1 class="headline">NEW CAREER AHEAD</h1>

  <svg class="direction-arrow" width="200" height="72" viewBox="0 0 200 72" aria-hidden="true">
    <polygon points="8,66 118,38 114,28 190,20 134,56 128,46 14,74" fill="var(--white)" opacity="0.85"/>
  </svg>

  <section class="frame frame--market">
    <div class="frame-photo" role="img" aria-label="Person with raised arms standing on the Great Wall of China"></div>
    <div class="frame-copy">
      <p class="lead">Expand your</p>
      <p class="body">Career opportunities<br>with the world's<br>largest market of<br>1.3 billion people</p>
    </div>
  </section>

  <section class="frame frame--city">
    <div class="frame-photo" role="img" aria-label="Modern Shanghai skyline seen through two opening doors"></div>
    <div class="frame-copy">
      <p class="lead">Do an MBA</p>
      <p class="body">In the world's<br>most dynamic<br>global city</p>
    </div>
    <svg class="enter-arrow" width="16" height="18" viewBox="0 0 16 18" aria-hidden="true">
      <path d="M8 17V3M2 8l6-6 6 6" stroke="var(--white)" stroke-width="2" fill="none"/>
    </svg>
  </section>

  <section class="frame frame--school">
    <div class="frame-photo" role="img" aria-label="Business school campus building with trees"></div>
    <div class="frame-copy">
      <p class="school-name"><span class="mark"></span>HALNU</p>
      <p class="body"><span class="rank">#1</span> Business school and ranked #15 in the world by the Weekly Arbiter - <span class="cta">Click here</span></p>
    </div>
  </section>
</main>
</body>
</html>
```